Quenford Pier Hall Museum Website (Design Only)

The Quenford Pier Hall is a newly renovated historical building in lower Manhattan. We are building a website for them so that tours and events can be scheduled. We have provided typography requirements along with many photographs. You are free to be creative with the use of the photographs in your design. There is no specific brand or color guidelines but the client did specify that they wanted the website to be clean, simple and elegant BUT to also reflect the vintage colors and feeling of the building. Please do NOT design the logo as we have a separate contest for the logo. We have provided a mock up of all website pages that we would like designed. however we encourage you to design and submit the home page an a few other pages first so we can provide feedback. The designs that you provide must be compatible with Wix.

```html
<!DOCTYPE html>
<html lang="en">
<head>
<meta charset="utf-8">
<title>Quenford Pier Hall</title>
<link href="https://fonts.googleapis.com/css2?family=Jost:wght@400;500;600;700&family=Arimo:wght@400&display=swap" rel="stylesheet">
<style>
:root{
  --paper:#ddd8c6;
  --paper-light:#e6e2d3;
  --green:#6aa656;
  --green-dark:#4f8a3f;
  --green-soft:#8cc277;
  --ink:#2f2f2c;
  --gray:#4c4c48;
  --footer:#1c1c1c;
  --white:#fff;
  --photo-top:#a8987a;
  --photo-bottom:#5e5638;
}
*{margin:0;padding:0;box-sizing:border-box}
html,body{width:761px;height:1200px;overflow:hidden}
body{background:var(--paper);font-family:"Jost",sans-serif;color:var(--ink);position:relative}
.page{position:relative;width:761px;height:1200px;overflow:hidden;
  background:radial-gradient(ellipse at 50% 20%,var(--paper-light) 0%,var(--paper) 70%)}
.hero{position:absolute;left:0;top:0;width:761px;height:596px;
  background:linear-gradient(180deg,var(--photo-top) 0%,var(--photo-bottom) 100%)}
.nav-ribbon{position:absolute;left:0;top:0;width:761px;height:125px}
.nav{position:absolute;top:43px;height:36px;display:flex;align-items:center;gap:13px;
  font-size:8.6px;font-weight:500;color:var(--white);letter-spacing:.1px;text-transform:uppercase;white-space:nowrap}
.nav.left{left:78px}
.nav.right{left:447px}
.logo{position:absolute;left:329px;top:6px;width:113px;height:113px;border-radius:50%;
  background:var(--paper);border:1.5px solid var(--green-soft);
  display:flex;align-items:center;justify-content:center;text-align:left}
.logo span{font-size:12.5px;line-height:14px;font-weight:400;color:var(--ink)}
.scroll-down{position:absolute;left:358px;top:558px;width:74px;height:74px;border-radius:50%;
  background:var(--paper);display:flex;align-items:center;justify-content:center}
.scroll-down div{width:62px;height:62px;border-radius:50%;background:var(--green-soft);
  display:flex;align-items:center;justify-content:center}
.welcome{position:absolute;left:0;top:644px;width:761px;text-align:center}
.welcome h1{font-weight:400;font-size:27px;line-height:31px;color:var(--ink)}
.welcome h1 strong{display:block;font-weight:700;font-size:28px;letter-spacing:.3px}
.welcome hr{width:63px;margin:10px auto 0;border:0;border-top:1.5px solid var(--green-soft)}
.welcome p{margin:10px auto 0;width:575px;font-size:10.6px;line-height:17.5px;color:var(--ink)}
.card{position:absolute;top:798px;width:197px}
.card .frame{width:197px;height:200px;background:#eeece4;padding:7px;box-shadow:0 1px 2px rgba(0,0,0,.12)}
.card .photo{width:183px;height:182px}
.card .ribbon{position:absolute;left:0;top:181px;width:197px;height:40px}
.card .ribbon span{position:absolute;left:27px;top:7px;width:144px;height:31px;
  display:flex;align-items:center;justify-content:center;color:var(--white);
  font-weight:700;font-size:14px;letter-spacing:.4px}
.card p{margin-top:36px;text-align:center;font-family:"Arimo",sans-serif;font-size:10.4px;
  line-height:17.5px;color:var(--gray)}
.card .btn{display:block;margin:8px auto 0;width:95px;height:29px;border:1.3px solid var(--green);
  border-radius:15px;text-align:center;line-height:27px;font-size:10px;color:var(--ink)}
.footer{position:absolute;left:0;top:1150px;width:761px;height:50px;background:var(--footer);
  color:var(--white);font-size:8.8px;text-align:center;line-height:48px}
</style>
</head>
<body>
<div class="page">
  <section class="hero" role="img" aria-label="Photograph of the ornate ferry terminal facade seen from below"></section>

  <svg class="nav-ribbon" width="761" height="125" viewBox="0 0 761 125">
    <polygon points="45,35 87,35 87,63 45,63 55,49" fill="var(--green-dark)"/>
    <polygon points="716,35 674,35 674,63 716,63 706,49" fill="var(--green-dark)"/>
    <rect x="71" y="43" width="619" height="36" fill="var(--green)"/>
  </svg>
  <nav class="nav left"><span>About the Building</span><span>Calendar</span><span>Public Exhibitions</span></nav>
  <nav class="nav right"><span>Tour the Building</span><span>Plan Your Visit</span><span>Contact Us</span></nav>
  <div class="logo"><span>Quenford<br>Pier Hall</span></div>

  <div class="scroll-down"><div>
    <svg width="14" height="30" viewBox="0 0 14 30"><path d="M7 1V28M2 23l5 5 5-5" stroke="#fff" stroke-width="1" fill="none"/></svg>
  </div></div>

  <section class="welcome">
    <h1>WELCOME TO<strong>THE QUENFORD PIER HALL</strong></h1>
    <hr>
    <p>The majestic Quenford Pier Hall is located at the southern tip of Manhattan. Built in 1909, the building is the last remaining historic working ferry terminal in New York City.</p>
  </section>

  <article class="card" style="left:71px">
    <div class="frame"><div class="photo" role="img" aria-label="Photograph of the lower Manhattan skyline across the water" style="background:linear-gradient(#8fa6d8 0%,#c9d3e4 45%,#8d8570 70%,#52606e 100%)"></div></div>
    <svg class="ribbon" width="197" height="40"><polygon points="7,0 40,0 40,24 7,24 14,12" fill="var(--green-dark)"/><polygon points="190,0 157,0 157,24 190,24 183,12" fill="var(--green-dark)"/><rect x="27" y="7" width="144" height="31" fill="var(--green)"/></svg>
    <div class="ribbon"><span>HOURS</span></div>
    <p>Check the calendar to see our<br>hours of operation.</p>
    <span class="btn">Go to Calendar</span>
  </article>

  <article class="card" style="left:283px">
    <div class="frame"><div class="photo" role="img" aria-label="Photograph of the terminal front under a blue sky" style="background:linear-gradient(#2f7fd0 0%,#9cc8ef 45%,#7a6a48 70%,#3d3a2a 100%)"></div></div>
    <svg class="ribbon" width="197" height="40"><polygon points="7,0 40,0 40,24 7,24 14,12" fill="var(--green-dark)"/><polygon points="190,0 157,0 157,24 190,24 183,12" fill="var(--green-dark)"/><rect x="27" y="7" width="144" height="31" fill="var(--green)"/></svg>
    <div class="ribbon"><span>WHAT TO SEE</span></div>
    <p>Our building hosts exhibitions<br>of all kinds</p>
    <span class="btn">Exhibitions</span>
  </article>

  <article class="card" style="left:494px">
    <div class="frame"><div class="photo" role="img" aria-label="Photograph of the historic building corner against a cloudy sky" style="background:linear-gradient(#9fb4d4 0%,#d8dde4 35%,#7b6a45 70%,#3e3f2a 100%)"></div></div>
    <svg class="ribbon" width="197" height="40"><polygon points="7,0 40,0 40,24 7,24 14,12" fill="var(--green-dark)"/><polygon points="190,0 157,0 157,24 190,24 183,12" fill="var(--green-dark)"/><rect x="27" y="7" width="144" height="31" fill="var(--green)"/></svg>
    <div class="ribbon"><span>HISTORY</span></div>
    <p>A building of New York<br>City’s maritime history.</p>
    <span class="btn">Our Mission</span>
  </article>

  <footer class="footer">© Copyrights 2022-Quenford Pier Hall.All Rights Reserved.</footer>
</div>
</body>
</html>
```